International Manufacturing Business Needs A Heavy Hitting Wordpress Design!

We need wordpress template designs for a new website for our UK based International company Tolvane Engineering Ltd. We manufacture and supply steel security doors and window units. We would like designs that feature the black and yellow industrial "stripes" that can be seen at our current site www.tolvadoors.com. The final design should communicate strength, power and weight to represent the quality of the products and the security that they provide.

It feels like we need 3 different types of page to be able to be created as per the current website at www.tolvasecuredoors.com.

Homepage
Products/Accessories
Leadtimes/Downloads/Contact

It may be that 3 different page types can be created with one template. I'm totally open to this.

I don't like the way that the site currently handles product images, nobody wants to click on even thumbnail to see the product. http://tolvasecuredoors.com/products/personnel-doors/

Totally open to suggestions on layout to enable the feeling outlined in the brief above.

Please ask if anything is not clear or you need answers to drill down on specifics.

Sick

Target Market(s)

Businesses that buy steel doors

Font styles to use
Sans Serif
Other font styles liked:
• Copperplate Gothic Bold - For Company Name but we are open to suggestions

Colors

Designer to choose colors to be used in the design.

Requirements
Must have
• Professional looking, clean design
• Conveys strength, power and weight to represent the quality of the products, the characteristics of steel and the security that they provide.
• Incorporates black and yellow stripes of our branding
• Ability to create pages with content as seen at www.tolvasecuredoors.com
• A better way of showing the product images
Nice to have
• If possible. a design that gives off the feeling that not only do we supply the products we also make them in house too. I don't know what this looks like but a way of differentiating between a supply only business and one that manufacturers the product too.
Should not have
• We don't like the current thumbnail method of showing the product images

```html
<!DOCTYPE html>
<html lang="en">
<head>
<meta charset="utf-8">
<title>Tolvane Engineering Ltd – Steel Security Doors</title>
<link href="https://fonts.googleapis.com/css2?family=Jost:wght@400;500;600&family=Mulish:wght@400;600&display=swap" rel="stylesheet">
<style>
:root{
  --yellow:#f7c51c;
  --dark:#262626;
  --dark-2:#2f2f2f;
  --olive:#4d4722;
  --text:#222;
  --muted:#6b6b6b;
  --line:#e6e6e6;
  --steel:#5b6068;
  --white:#fff;
}
*{box-sizing:border-box;margin:0;padding:0}
html,body{width:1200px;height:2510px;overflow:hidden}
body{position:relative;background:var(--white);font-family:"Mulish",sans-serif;color:var(--text)}
.abs{position:absolute}
.head-font{font-family:"Jost",sans-serif}
.btn{position:absolute;display:flex;align-items:center;justify-content:center;font-family:"Jost",sans-serif;font-size:12px;letter-spacing:1.5px;text-transform:uppercase;font-weight:500}
.btn-yellow{background:var(--yellow);color:var(--dark)}
.btn-outline{border:1.5px solid var(--yellow);color:var(--dark);background:var(--white)}

/* header */
.site-header{position:absolute;left:0;top:0;width:1200px;height:104px}
.brand{position:absolute;left:156px;top:30px;display:flex;align-items:center;gap:12px}
.brand-mark{width:34px;height:34px;background:var(--dark)}
.brand-name{font-family:"Jost",sans-serif;font-weight:600;font-size:26px;color:var(--dark);letter-spacing:.5px;line-height:1}
.call{position:absolute;left:578px;top:36px;display:flex;align-items:center;gap:10px;font-family:"Jost",sans-serif;font-size:21px}
.call .label{color:var(--yellow);font-weight:500}
.call .num{color:var(--dark);font-weight:500}

/* nav */
.main-nav{position:absolute;left:0;top:104px;width:1200px;height:40px;background:var(--dark)}
.main-nav svg{position:absolute;left:0;top:0}
.nav-item{position:absolute;top:0;height:40px;line-height:40px;font-family:"Jost",sans-serif;font-size:12.5px;letter-spacing:1.2px;color:var(--white);text-transform:uppercase;font-weight:500}
.nav-item.active{background:var(--yellow);color:var(--dark);width:107px;text-align:center}
.dropdown{position:absolute;left:805px;top:161px;width:188px;height:78px;background:var(--yellow);padding:14px 20px;z-index:5}
.dropdown span{display:block;font-family:"Jost",sans-serif;font-size:12.5px;letter-spacing:1.2px;color:var(--white);font-weight:500}
.dropdown .sep{height:0;border-top:1px dashed rgba(255,255,255,.8);margin:8px 0 6px}

/* hero */
.hero{position:absolute;left:0;top:144px;width:1200px;height:432px;background:linear-gradient(180deg,#6d6e6a 0%,#9a9b97 40%,#7f7b73 75%,#5e5249 100%)}
.hero::after{content:"";position:absolute;inset:0;background:rgba(0,0,0,.22)}
.hero-title{position:absolute;left:0;top:292px;width:1200px;text-align:center;font-family:"Jost",sans-serif;font-weight:500;font-size:24px;line-height:31px;color:var(--white);z-index:2}

/* why */
.section-title{font-family:"Jost",sans-serif;font-weight:500;color:var(--dark)}
.rule{position:absolute;height:2px;background:var(--yellow)}
.why-title{position:absolute;left:156px;top:680px;font-size:25px}
.why-list{position:absolute;left:156px;top:748px;width:510px;list-style:none}
.why-list li{position:relative;padding-left:22px;font-size:11.5px;line-height:18px;color:var(--muted);margin-bottom:17px}
.why-list li svg{position:absolute;left:0;top:3px}

/* quote */
.quote-back{position:absolute;left:728px;top:640px;width:228px;height:227px;background:linear-gradient(135deg,var(--olive) 0 40%,var(--dark) 40%)}
.quote-card{position:absolute;left:752px;top:665px;width:279px;height:386px;background:var(--white);box-shadow:0 4px 18px rgba(0,0,0,.14)}
.quote-card h3{font-family:"Jost",sans-serif;font-weight:500;font-size:23px;text-align:center;margin-top:17px;color:var(--dark)}
.field{position:absolute;left:0;width:279px;height:49px;border-top:1px solid var(--line);padding-left:23px;line-height:49px;font-size:11px;color:#888}
.quote-foot{position:absolute;left:23px;top:346px;display:flex;align-items:center;gap:8px;font-family:"Jost",sans-serif;font-size:14px;color:var(--dark)}

/* products */
.center-title{position:absolute;left:0;width:1200px;text-align:center;font-size:23px}
.product-card{position:absolute;top:1183px;width:279px;height:206px}
.product-card .photo{height:158px}
.product-card .name{height:48px;line-height:48px;text-align:center;font-family:"Jost",sans-serif;font-weight:500;font-size:15px;color:var(--dark);border-bottom:3px solid var(--yellow)}
.product-card.active .name{background:var(--yellow)}
.slider-arrow{position:absolute;top:1255px}

/* band */
.cta-band{position:absolute;left:0;top:1520px;width:1200px;height:120px;background:var(--dark);overflow:hidden}
.cta-band svg{position:absolute;left:0;top:0}
.cta-text{position:absolute;left:231px;top:28px;font-family:"Jost",sans-serif;font-weight:500;font-size:17px;line-height:21px;color:var(--white)}

/* latest */
.latest-name{position:absolute;left:156px;top:1793px;font-family:"Jost",sans-serif;font-weight:600;font-size:16px}
.latest-text{position:absolute;left:156px;top:1832px;width:420px;font-size:11.5px;line-height:19px;color:var(--muted)}
.explore{position:absolute;left:156px;top:1905px;font-family:"Jost",sans-serif;font-size:10.5px;letter-spacing:1px;color:var(--dark)}
.round{position:absolute;top:1953px;width:26px;height:26px;border:1.5px solid var(--yellow);border-radius:50%}
.latest-frame{position:absolute;left:639px;top:1771px;width:404px;height:233px;background:#e4e7eb}
.latest-photo{position:absolute;left:24px;top:24px;width:356px;height:185px;background:linear-gradient(90deg,#d8dadd 0 25%,#4c5158 25% 100%)}

/* partners */
.partner{position:absolute;top:2090px;width:107px;height:47px}

/* footer */
.site-footer{position:absolute;left:0;top:2153px;width:1200px;height:357px;background:var(--dark-2);overflow:hidden}
.site-footer svg.stripes{position:absolute;left:0;top:0}
.f-col{position:absolute;top:62px;width:264px}
.f-col h4{font-family:"Jost",sans-serif;font-weight:500;font-size:14px;color:var(--white);padding-bottom:9px;border-bottom:1px solid #555}
.f-contact p{font-size:11px;line-height:19px;color:var(--white);margin-top:12px}
.f-contact p:first-child{margin-top:16px}
.f-contact b{color:var(--yellow);font-weight:600}
.f-links{position:absolute;top:40px;list-style:none}
.f-links li{font-size:11px;color:var(--white);line-height:24px}
.f-links li::before{content:"→ ";color:var(--white)}
.f-links li.current{color:var(--yellow)}
.f-links li.current::before{color:var(--yellow)}
.mail-text{font-size:11px;line-height:18px;color:var(--white);margin-top:16px}
.mail-input{margin-top:10px;height:32px;background:var(--steel);color:#e6e6e6;font-size:11px;line-height:32px;padding-left:12px}
.f-bottom{position:absolute;left:131px;top:278px;width:938px;border-top:1px solid #444}
.copy{position:absolute;left:156px;top:312px;font-size:11px;color:var(--white)}
.copy span{color:var(--yellow);text-decoration:underline}
.social-label{position:absolute;left:735px;top:313px;font-family:"Jost",sans-serif;font-size:10px;letter-spacing:1px;color:var(--yellow);font-weight:500}
.social{position:absolute;top:307px;width:22px;height:22px;border-radius:50%;background:#5a5a5a}
.to-top{position:absolute;left:991px;top:278px;width:52px;height:79px;background:var(--steel)}
</style>
</head>
<body>

<header class="site-header">
  <div class="brand"><span class="brand-mark"></span><span class="brand-name">TOLVANE</span></div>
  <div class="call">
    <span class="label">Call Us:</span>
    <svg width="22" height="22" viewBox="0 0 22 22"><circle cx="11" cy="11" r="10" fill="none" stroke="#f7c51c" stroke-width="1.6"/><path d="M7.5 6.5l2 0 1 3-1.3 1c.7 1.4 1.6 2.3 3 3l1-1.3 3 1v2c-5 .4-9-3.7-8.7-8.7z" fill="#f7c51c"/></svg>
    <span class="num">+44 (0)1632 960 300</span>
  </div>
  <div class="btn btn-yellow" style="left:916px;top:33px;width:127px;height:36px;font-size:11px">Online Order</div>
</header>

<nav class="main-nav">
  <svg width="1200" height="40"><polygon points="0,0 60,0 20,40 0,40" fill="#4d4722"/><polygon points="1110,0 1200,0 1200,40 1070,40" fill="#4d4722"/></svg>
  <span class="nav-item" style="left:206px">Home</span>
  <span class="nav-item" style="left:317px">Products</span>
  <span class="nav-item" style="left:456px">Accessories</span>
  <span class="nav-item" style="left:623px">Delivery &amp; Lead Times</span>
  <span class="nav-item active" style="left:805px">Info</span>
  <span class="nav-item" style="left:945px">Contact Us</span>
</nav>
<div class="dropdown"><span>Downloads</span><div class="sep"></div><span>Technical Videos</span></div>

<section class="hero" role="img" aria-label="Photograph of a timber-clad house with a white veranda"></section>
<h1 class="hero-title">Tolvane Have Forged a Reputation for Affordable,<br>High Quality Steel Doors</h1>
<div class="btn btn-yellow" style="left:544px;top:383px;width:127px;height:32px;font-size:11px;z-index:2">Explore More</div>

<section>
  <h2 class="section-title why-title">Why Choose Us?</h2>
  <div class="rule" style="left:156px;top:718px;width:75px"></div>
  <ul class="why-list">
    <li><svg width="11" height="11"><rect x=".5" y=".5" width="10" height="10" fill="none" stroke="#f7c51c"/><path d="M2.5 5.5l2 2 4-4.5" fill="none" stroke="#f7c51c" stroke-width="1.4"/></svg>Tolvane security doors combine a high level of security with exceptional value.</li>
    <li><svg width="11" height="11"><rect x=".5" y=".5" width="10" height="10" fill="none" stroke="#f7c51c"/><path d="M2.5 5.5l2 2 4-4.5" fill="none" stroke="#f7c51c" stroke-width="1.4"/></svg>Our superior quality and proven reliability has made us the first choice for a wide range of companies no matter what their requirement or application.</li>
    <li><svg width="11" height="11"><rect x=".5" y=".5" width="10" height="10" fill="none" stroke="#f7c51c"/><path d="M2.5 5.5l2 2 4-4.5" fill="none" stroke="#f7c51c" stroke-width="1.4"/></svg>We place particular emphasis on continuous development and twelve years experience ensures that we are always ahead of the competition and that we can react quickly to customer's requirements.</li>
    <li><svg width="11" height="11"><rect x=".5" y=".5" width="10" height="10" fill="none" stroke="#f7c51c"/><path d="M2.5 5.5l2 2 4-4.5" fill="none" stroke="#f7c51c" stroke-width="1.4"/></svg>Each and every Tolvane product is subject to our fifty point quality control process before it is dispatched.</li>
  </ul>
  <div class="btn btn-outline" style="left:156px;top:972px;width:129px;height:34px;font-size:11px">Contact Us</div>
</section>

<div class="quote-back"></div>
<form class="quote-card">
  <h3>Get A Free Quote</h3>
  <div class="field" style="top:66px">Name</div>
  <div class="field" style="top:115px">Email</div>
  <div class="field" style="top:164px">Phone</div>
  <div class="field" style="top:213px">Address</div>
  <div class="field" style="top:262px">Type of Doors
    <svg style="position:absolute;right:22px;top:22px" width="8" height="5"><path d="M0 0h8L4 5z" fill="#999"/></svg></div>
  <div class="field" style="top:311px;height:75px"></div>
  <div class="quote-foot">
    <svg width="20" height="20" viewBox="0 0 22 22"><circle cx="11" cy="11" r="10" fill="none" stroke="#f7c51c" stroke-width="1.6"/><path d="M7.5 6.5l2 0 1 3-1.3 1c.7 1.4 1.6 2.3 3 3l1-1.3 3 1v2c-5 .4-9-3.7-8.7-8.7z" fill="#f7c51c"/></svg>
    (0)1632 960 300
  </div>
  <div class="btn btn-yellow" style="left:219px;top:331px;width:73px;height:34px;font-size:10.5px;letter-spacing:1px">Get a Quote</div>
</form>

<section>
  <h2 class="section-title center-title" style="top:1108px">Our Products</h2>
  <div class="rule" style="left:563px;top:1147px;width:74px"></div>
  <svg class="slider-arrow" style="left:122px" width="10" height="16"><path d="M8 1L2 8l6 7" fill="none" stroke="#333" stroke-width="2"/></svg>
  <svg class="slider-arrow" style="left:1067px" width="10" height="16"><path d="M2 1l6 7-6 7" fill="none" stroke="#f7c51c" stroke-width="2"/></svg>
  <div class="product-card" style="left:156px"><div class="photo" role="img" aria-label="White double personnel doors in a bright room" style="background:linear-gradient(180deg,#ececec 0 75%,#b89e82 75%)"></div><div class="name">Personnel Doors</div></div>
  <div class="product-card active" style="left:460px"><div class="photo" role="img" aria-label="Red fire exit door in a white corridor" style="background:linear-gradient(90deg,#d4d6d6 0 38%,#cf3d28 38% 75%,#e5e5e5 75%)"></div><div class="name">Fire Exit Doors</div></div>
  <div class="product-card" style="left:765px"><div class="photo" role="img" aria-label="Large glazed opening looking onto a snowy landscape" style="background:linear-gradient(180deg,#8a7768 0%,#c9ccc9 45%,#8f8d86 100%)"></div><div class="name">Blank Doors</div></div>
  <div class="btn btn-outline" style="left:519px;top:1421px;width:161px;height:34px;font-size:11px">View All Products</div>
</section>

<section class="cta-band">
  <svg width="1200" height="120"><polygon points="0,0 330,0 230,120 0,120" fill="#4d4722"/><polygon points="640,0 900,0 820,120 560,120" fill="#4d4722" opacity=".85"/><polygon points="1080,0 1200,0 1200,120 1000,120" fill="#4d4722"/></svg>
  <p class="cta-text">We Manufacture products to the highest specification,<br>combine with a Rigorous Quality control system and an extensive<br>after-sales service.</p>
  <div class="btn btn-yellow" style="left:840px;top:45px;width:128px;height:32px;font-size:11px">Contact Now!</div>
</section>

<section>
  <h2 class="section-title center-title" style="top:1697px">Our Latest Products</h2>
  <div class="rule" style="left:563px;top:1738px;width:74px"></div>
  <h3 class="latest-name">Anti-Vandal Shroud</h3>
  <p class="latest-text">Tolvane Engineering's anti-vandal shroud has been designed to offer increased security protection for the standard 10-point locking personnel door ...</p>
  <span class="explore">EXPLORE MORE →</span>
  <span class="round" style="left:155px"><svg width="26" height="26"><path d="M14 9l-4 4 4 4" fill="none" stroke="#333" stroke-width="1.5"/></svg></span>
  <span class="round" style="left:190px"><svg width="26" height="26"><path d="M11 9l4 4-4 4" fill="none" stroke="#333" stroke-width="1.5"/></svg></span>
  <div class="latest-frame"><div class="latest-photo" role="img" aria-label="Close-up of a multi-point locking mechanism and steel door handle"></div></div>
</section>

<section>
  <div class="rule" style="left:308px;top:2069px;width:583px;height:1px;background:#ddd"></div>
  <div class="partner" style="left:340px;background:#e6ebf3" role="img" aria-label="Trade association badge"></div>
  <div class="partner" style="left:536px;border:2px solid #333" role="img" aria-label="Certification badge"></div>
  <div class="partner" style="left:732px;background:#8a5a3a" role="img" aria-label="Industry association badge"></div>
</section>

<footer class="site-footer">
  <svg class="stripes" width="1200" height="120"><polygon points="0,0 170,0 50,100 0,100" fill="#4d4722"/><polygon points="980,0 1200,0 1200,100 1100,100" fill="#4d4722"/></svg>
  <div class="f-col f-contact" style="left:156px">
    <h4>Contact Us</h4>
    <p><b>ADDRESS:</b> Harlow Ridge Mill Lane<br>Brackwick Dunmoor UK DN99 4QT</p>
    <p><b>PHONE:</b> +44 (0) 1632 960300</p>
    <p><b>FAX:</b> +44 (0) 1632 960400</p>
    <p><b>EMAIL:</b> <u>sales@tolvadoors.com</u></p>
  </div>
  <div class="f-col" style="left:467px">
    <h4>Browse Our Website</h4>
    <ul class="f-links" style="left:0"><li class="current">Home</li><li>Products</li><li>Accessories</li><li>Delivery &amp; Lead Times</li></ul>
    <ul class="f-links" style="left:146px"><li>Info</li><li>Contact Us</li></ul>
  </div>
  <div class="f-col" style="left:780px">
    <h4>Join our Mailing List</h4>
    <p class="mail-text">You Want to get Update about anything News?<br>Join our newsletter</p>
    <div class="mail-input">Enter Your Email...</div>
    <div class="btn btn-yellow" style="position:relative;margin-top:11px;width:96px;height:32px;font-size:11px">Send</div>
  </div>
  <div class="f-bottom"></div>
  <p class="copy">© 2018 <span>Tolvane Engineering LTD.</span> All Right Reserved</p>
  <span class="social-label">GET SOCIAL:</span>
  <span class="social" style="left:820px"></span>
  <span class="social" style="left:850px;background:var(--yellow)"></span>
  <span class="social" style="left:880px"></span>
  <span class="social" style="left:912px"></span>
  <span class="social" style="left:943px"></span>
  <div class="to-top"><svg width="52" height="79"><path d="M21 39l5-5 5 5M21 45l5-5 5 5" fill="none" stroke="#fff" stroke-width="1.5"/></svg></div>
</footer>

</body>
</html>
```